IT Consulting, IT Beacon, Software Development, Network Solutions, Hosting

Attached is logo for our company, we just was the designers to come up with creative ideas to use the logo and the theme to come with creative and energetic business cards that leave an impression and stick in people's head.

Target Market(s)

Medical, Law, Entertainment, Real estate, any small to medium size business.

Industry/Entity Type

Business

Font styles to use
Serif
Sans Serif

```html
<!DOCTYPE html>
<html lang="en">
<head>
<meta charset="utf-8">
<title>IT Beacon Business Card</title>
<link href="https://fonts.googleapis.com/css2?family=Lato:ital,wght@0,400;0,700;1,400&display=swap" rel="stylesheet">
<style>
  :root {
    --bg: #d6d6d6;
    --card: #171717;
    --accent: #f6c90e;
    --text-light: #ffffff;
    --text-muted: #9a9a9a;
  }
  html, body {
    margin: 0;
    width: 1200px;
    height: 926px;
    overflow: hidden;
    background: var(--bg);
    font-family: "Lato", Arial, sans-serif;
  }
  .sheet {
    position: relative;
    width: 1200px;
    height: 926px;
    display: flex;
    align-items: center;
    justify-content: center;
    gap: 40px;
  }
  .card {
    position: relative;
    width: 540px;
    height: 309px;
    background: var(--card);
    box-shadow: 0 10px 24px rgba(0,0,0,0.25);
    overflow: hidden;
  }
  .card-front .accent-band {
    position: absolute;
    top: 0; left: 0; right: 0;
    height: 7px;
    background: var(--accent);
  }
  .identity {
    position: absolute;
    left: 36px;
    top: 42px;
  }
  .person-name {
    margin: 0;
    color: var(--text-light);
    font-size: 22px;
    font-weight: 400;
    letter-spacing: 0.2px;
  }
  .person-name strong { font-weight: 700; }
  .person-title {
    margin: 2px 0 0;
    color: var(--text-muted);
    font-size: 11px;
    font-style: italic;
  }
  .contact-list {
    position: absolute;
    left: 36px;
    list-style: none;
    margin: 0;
    padding: 0;
    color: var(--text-muted);
    font-size: 14px;
    line-height: 19px;
    letter-spacing: 0.6px;
  }
  .contact-list.address-block { top: 122px; }
  .contact-list.web-block { top: 216px; font-size: 13px; line-height: 21px; }
  .contact-list li {
    display: flex;
    align-items: flex-start;
    gap: 8px;
  }
  .contact-list .icon {
    flex: 0 0 12px;
    width: 12px;
    height: 12px;
    margin-top: 4px;
    fill: var(--accent);
    stroke: var(--accent);
  }
  .wordmark {
    position: absolute;
    color: var(--accent);
    font-weight: 400;
    letter-spacing: 2px;
    white-space: nowrap;
  }
  .card-front .wordmark {
    right: 30px;
    bottom: 26px;
    font-size: 32px;
  }
  .card-back .wordmark {
    left: 50%;
    top: 50%;
    transform: translate(-50%, -50%);
    font-size: 34px;
  }
</style>
</head>
<body>
<main class="sheet">
  <section class="card card-front" aria-label="Business card front">
    <div class="accent-band"></div>
    <div class="identity">
      <h1 class="person-name">Dana <strong>Reyes</strong></h1>
      <p class="person-title">Title goes here</p>
    </div>
    <ul class="contact-list address-block">
      <li>
        <svg class="icon" viewBox="0 0 12 12" aria-hidden="true"><path d="M2 3.5c0-1 1-1.5 4-1.5s4 .5 4 1.5v1H8v-1H4v1H2z" stroke="none"/><rect x="3" y="5.5" width="6" height="4.5" rx="0.8" stroke="none"/></svg>
        <span>555-014-2290</span>
      </li>
      <li>
        <svg class="icon" viewBox="0 0 12 12" aria-hidden="true"><path d="M6 1.5 1 6h1.5v4.5h2.5V8h2v2.5h2.5V6H11z" stroke="none"/></svg>
        <span>48 Harbor Lane, Unit 12,<br>Crest Bldg, Ridgefield,<br>NJ 07410</span>
      </li>
    </ul>
    <ul class="contact-list web-block">
      <li>
        <svg class="icon" viewBox="0 0 12 12" aria-hidden="true"><rect x="1" y="2.5" width="10" height="7" stroke="none"/><path d="M1.3 3 6 6.5 10.7 3" fill="none" stroke="#171717" stroke-width="1"/></svg>
        <span>itbeacon.example</span>
      </li>
      <li>
        <svg class="icon" viewBox="0 0 12 12" aria-hidden="true"><g fill="none" stroke-width="1.4"><rect x="1" y="5.5" width="5.5" height="3" rx="1.5" transform="rotate(-40 3.7 7)"/><rect x="5.5" y="3.5" width="5.5" height="3" rx="1.5" transform="rotate(-40 8.2 5)"/></g></svg>
        <span>dana@itbeacon.example</span>
      </li>
    </ul>
    <div class="wordmark">IT BEACON</div>
  </section>

  <section class="card card-back" aria-label="Business card back">
    <div class="wordmark">IT BEACON</div>
  </section>
</main>
</body>
</html>
```